Flyer for an autonomous utility vehicle to be used in campgrounds

I would like the design and files for printing of a brochure or flyer (options to be considered are appreciated) that utilizes the verbiage from the uploaded MILO Your Trailside Helper word document. I've included a video and some other items for reference or inspiration. The completed work should include images of driverless utility vehicles like the Quillet Drover or others in a campground setting autonomously picking up trash, delivering firewood, guiding recreational vehicle drivers to their camp sites, and providing security. Please ensure that any mention of MILO or MILO AV kit is trademarked and there is a disclaimer somewhere on the printed material that MILO and MILO A/V Kit are registered Trademarks of Vashti Automation.

```html
<!DOCTYPE html>
<html lang="en">
<head>
<meta charset="utf-8">
<title>MILO – Your Trailside Helper</title>
<link rel="stylesheet" href="https://fonts.googleapis.com/css2?family=Montserrat:wght@400;600;700;800;900&display=swap">
<style>
  :root{
    --forest:#1f4a2d;
    --forest-deep:#163a22;
    --orange:#f7931e;
    --orange-deep:#e8731a;
    --white:#ffffff;
    --mist:#d9e4dc;
  }
  *{margin:0;padding:0;box-sizing:border-box}
  html,body{width:732px;height:1200px;overflow:hidden;background:#e9e9e9}
  .flyer{position:relative;width:732px;height:1200px;background:var(--forest);overflow:hidden;font-family:'Montserrat',sans-serif;color:var(--white)}
  .hero-photo{position:absolute;top:0;right:0;width:360px;height:230px}
  .title-block{position:absolute;left:40px;top:30px}
  .brand{font-size:92px;font-weight:900;color:var(--orange);line-height:.9;letter-spacing:1px}
  .tagline{font-size:27px;font-weight:800;line-height:1.05;text-transform:uppercase;margin-top:6px}
  .tagline span{display:block;color:var(--orange)}
  .headline{position:absolute;left:40px;top:205px;width:390px;font-size:16px;font-weight:800;line-height:1.25;text-transform:uppercase}
  .intro{position:absolute;left:40px;top:258px;width:640px;font-size:10.5px;line-height:1.5;color:var(--mist)}
  .column{position:absolute;top:325px}
  .column.left{left:40px;width:310px}
  .column.right{left:390px;width:300px}
  .section-title{font-size:14px;font-weight:800;color:var(--orange);text-transform:uppercase;margin-bottom:12px;line-height:1.2}
  .feature-list{list-style:none}
  .feature-list li{display:flex;align-items:flex-start;gap:10px;margin-bottom:12px;font-size:10.5px;line-height:1.4;color:var(--mist)}
  .feature-list b{color:var(--white);font-weight:700}
  .num{flex:0 0 24px;height:24px;border-radius:50%;background:var(--orange);color:var(--white);font-weight:800;font-size:11px;display:flex;align-items:center;justify-content:center}
  .tick{flex:0 0 20px;height:20px;margin-top:1px}
  .right .section-title.second{margin-top:18px}
  .camp-photo{position:absolute;left:0;bottom:0;width:430px;height:440px}
  .cta{position:absolute;left:448px;top:800px;width:250px}
  .cta-title{font-size:20px;font-weight:900;line-height:1.15;text-transform:uppercase;color:var(--orange)}
  .cta-text{font-size:10.5px;line-height:1.5;color:var(--mist);margin-top:10px}
  .contact{list-style:none;margin-top:16px}
  .contact li{display:flex;align-items:center;gap:8px;font-size:11px;font-weight:600;margin-bottom:8px}
  .contact svg{flex:0 0 18px}
  .disclaimer{font-size:8.5px;line-height:1.4;color:var(--mist);margin-top:14px;width:230px}
  .corner-wave{position:absolute;right:0;bottom:0;width:300px;height:150px}
</style>
</head>
<body>
<main class="flyer">

  <svg class="hero-photo" viewBox="0 0 360 230" role="img" aria-label="Photo of campers around a glowing campfire at sunset with mountains behind">
    <defs>
      <linearGradient id="sunset" x1="0" y1="0" x2="0" y2="1">
        <stop offset="0" stop-color="#f2a24a"/>
        <stop offset=".45" stop-color="#b5552a"/>
        <stop offset="1" stop-color="#2b1a14"/>
      </linearGradient>
    </defs>
    <path d="M40 0 H360 V230 H140 C70 230 40 170 40 110 Z" fill="url(#sunset)"/>
    <path d="M30 0 C28 120 60 228 150 230" fill="none" stroke="var(--orange)" stroke-width="8"/>
  </svg>

  <header class="title-block">
    <h1 class="brand">MILO™</h1>
    <p class="tagline">Your Trailside<span>Helper</span></p>
  </header>

  <h2 class="headline">Reimagining the outdoors with smart, autonomous utility vehicles</h2>

  <p class="intro">The MILO™ Trailside Helper is the perfect blend of the MILO™ AV Kit and a rugged Quillet Drover platform, built to keep campgrounds clean, safe and welcoming while freeing staff to focus on guests.</p>

  <section class="column left">
    <h3 class="section-title">Guest &amp; Staff Support Features</h3>
    <ol class="feature-list">
      <li><span class="num">1</span><p><b>Trash Collection:</b> Scheduled pickups keep every site tidy.</p></li>
      <li><span class="num">2</span><p><b>Firewood Delivery:</b> Bundles arrive right at the campsite on request.</p></li>
      <li><span class="num">3</span><p><b>RV Guidance:</b> Leads drivers safely to their assigned sites.</p></li>
      <li><span class="num">4</span><p><b>Security Patrols:</b> Quiet night rounds with live alerts to staff.</p></li>
      <li><span class="num">5</span><p><b>Supply Runs:</b> Moves linens, tools and gear between buildings.</p></li>
      <li><span class="num">6</span><p><b>Guest Info:</b> Answers questions about trails, rules and events.</p></li>
      <li><span class="num">7</span><p><b>24/7 Operation:</b> Ready day or night, in any season.</p></li>
    </ol>
  </section>

  <section class="column right">
    <h3 class="section-title">Advanced Autonomy</h3>
    <ul class="feature-list">
      <li><svg class="tick" viewBox="0 0 20 20"><circle cx="10" cy="10" r="10" fill="var(--orange)"/><path d="M5.5 10.5l3 3 6-6.5" fill="none" stroke="#fff" stroke-width="2"/></svg><p><b>Obstacle Detection:</b> Sensors spot people, pets and debris.</p></li>
      <li><svg class="tick" viewBox="0 0 20 20"><circle cx="10" cy="10" r="10" fill="var(--orange)"/><path d="M5.5 10.5l3 3 6-6.5" fill="none" stroke="#fff" stroke-width="2"/></svg><p><b>Route Mapping:</b> Learns every loop, road and trail.</p></li>
      <li><svg class="tick" viewBox="0 0 20 20"><circle cx="10" cy="10" r="10" fill="var(--orange)"/><path d="M5.5 10.5l3 3 6-6.5" fill="none" stroke="#fff" stroke-width="2"/></svg><p><b>Remote Control:</b> Staff can take over from any device.</p></li>
      <li><svg class="tick" viewBox="0 0 20 20"><circle cx="10" cy="10" r="10" fill="var(--orange)"/><path d="M5.5 10.5l3 3 6-6.5" fill="none" stroke="#fff" stroke-width="2"/></svg><p><b>Low-Speed Safety:</b> Designed for busy, shared spaces.</p></li>
    </ul>
    <h3 class="section-title second">Smart, Scalable,<br>Sustainable</h3>
    <ul class="feature-list">
      <li><svg class="tick" viewBox="0 0 20 20"><circle cx="10" cy="10" r="10" fill="var(--orange)"/><path d="M5.5 10.5l3 3 6-6.5" fill="none" stroke="#fff" stroke-width="2"/></svg><p><b>Electric Power:</b> Quiet, zero-emission operation.</p></li>
      <li><svg class="tick" viewBox="0 0 20 20"><circle cx="10" cy="10" r="10" fill="var(--orange)"/><path d="M5.5 10.5l3 3 6-6.5" fill="none" stroke="#fff" stroke-width="2"/></svg><p><b>Fleet Ready:</b> Add units as your park grows.</p></li>
      <li><svg class="tick" viewBox="0 0 20 20"><circle cx="10" cy="10" r="10" fill="var(--orange)"/><path d="M5.5 10.5l3 3 6-6.5" fill="none" stroke="#fff" stroke-width="2"/></svg><p><b>Retrofit Kit:</b> Fits existing utility vehicles.</p></li>
    </ul>
  </section>

  <svg class="camp-photo" viewBox="0 0 430 440" role="img" aria-label="Photo of friends relaxing by a green tent at a lakeside campsite in golden light">
    <defs>
      <linearGradient id="campsite" x1="0" y1="0" x2="0" y2="1">
        <stop offset="0" stop-color="#9fc3d6"/>
        <stop offset=".4" stop-color="#6f8f5a"/>
        <stop offset=".75" stop-color="#c7a33d"/>
        <stop offset="1" stop-color="#5d6b2a"/>
      </linearGradient>
    </defs>
    <path d="M0 40 C90 0 250 0 330 40 C400 80 410 180 410 440 H0 Z" fill="url(#campsite)"/>
    <path d="M330 40 C405 85 420 190 420 440" fill="none" stroke="var(--orange)" stroke-width="10"/>
  </svg>

  <section class="cta">
    <h3 class="cta-title">Transform your campground experience!</h3>
    <p class="cta-text">Bring smart autonomy to your park and give guests a stay they will remember.</p>
    <ul class="contact">
      <li><svg viewBox="0 0 18 18"><circle cx="9" cy="9" r="9" fill="var(--orange)"/><path d="M6 4.5l2 2-1 1.3c.6 1.4 1.8 2.6 3.2 3.2l1.3-1 2 2-1 1.5c-3.5-.3-7.2-4-7.5-7.5z" fill="#fff"/></svg>(555) 014-2290</li>
      <li><svg viewBox="0 0 18 18"><circle cx="9" cy="9" r="9" fill="var(--orange)"/><rect x="4.5" y="6" width="9" height="6.5" fill="none" stroke="#fff" stroke-width="1.3"/><path d="M4.5 6l4.5 3.6L13.5 6" fill="none" stroke="#fff" stroke-width="1.3"/></svg>hello@miloav.example</li>
      <li><svg viewBox="0 0 18 18"><circle cx="9" cy="9" r="9" fill="var(--orange)"/><circle cx="9" cy="9" r="4.5" fill="none" stroke="#fff" stroke-width="1.3"/><path d="M4.5 9h9M9 4.5c-2 2.5-2 6.5 0 9M9 4.5c2 2.5 2 6.5 0 9" fill="none" stroke="#fff" stroke-width="1"/></svg>www.miloav.example</li>
    </ul>
    <p class="disclaimer">MILO™ and MILO™ A/V Kit are registered Trademarks of Vashti Automation.</p>
  </section>

  <svg class="corner-wave" viewBox="0 0 300 150" aria-hidden="true">
    <path d="M0 150 C80 140 180 110 300 20 V150 Z" fill="var(--orange)"/>
    <path d="M120 150 C190 135 250 105 300 70 V150 Z" fill="var(--orange-deep)"/>
  </svg>

</main>
</body>
</html>
```